Postcard Design

Northgate Tidy Works Company Inc, is a air duct cleaning, dryer vent cleaning & pressure washing company, we would like this postcard to focus fully on our pressure washing specials for the season.

Industry/Entity Type

It Company

```html
<!DOCTYPE html>
<html lang="en">
<head>
<meta charset="utf-8">
<title>Northgate Tidy Works – Pressure Washing Postcard</title>
<link rel="stylesheet" href="https://fonts.googleapis.com/css2?family=Lato:ital,wght@0,400;0,700;0,900;1,700&family=Oswald:wght@600&family=Mulish:wght@800&display=swap">
<style>
  :root {
    --teal: #1fa3ad;
    --teal-light: #4cc3cc;
    --teal-dark: #11838c;
    --yellow: #f5cf2e;
    --yellow-soft: #fbe27a;
    --ink: #1e1e1e;
    --bar: #2a2a2a;
    --white: #ffffff;
    --page: #e9e9e9;
    --text: #333333;
  }
  * { box-sizing: border-box; margin: 0; padding: 0; }
  html, body { width: 902px; height: 1200px; overflow: hidden; }
  body { background: var(--page); font-family: "Lato", Arial, sans-serif; position: relative; }

  .postcard {
    position: absolute; left: 38px; width: 826px; height: 455px;
    background: var(--white); overflow: hidden;
    box-shadow: 0 4px 14px rgba(0,0,0,.25);
  }
  .postcard--front { top: 70px; }
  .postcard--back { top: 665px; }
  .postcard .shapes { position: absolute; inset: 0; width: 100%; height: 100%; }

  /* front */
  .brand {
    position: absolute; left: 128px; top: 38px;
    display: flex; align-items: center; gap: 10px;
    font-family: "Lato", sans-serif; font-weight: 900; font-size: 30px;
    color: var(--teal); line-height: 1;
  }
  .brand__mark { width: 18px; height: 18px; border-radius: 50%; background: var(--yellow); }
  .services-tab {
    position: absolute; left: 372px; top: 258px; width: 256px; height: 54px;
    background: linear-gradient(90deg, var(--yellow) 0%, var(--yellow) 60%, var(--yellow-soft) 100%);
    border-radius: 0 0 12px 0;
    box-shadow: 0 4px 6px rgba(0,0,0,.18);
    font-family: "Oswald", sans-serif; font-size: 30px; line-height: 54px;
    padding-left: 36px; color: var(--ink);
  }
  .services-tab .accent { color: var(--teal-dark); }
  .services-list {
    position: absolute; left: 412px; top: 336px; list-style: none;
    font-weight: 700; font-style: italic; font-size: 16px; color: var(--ink);
  }
  .services-list li { position: relative; padding-left: 24px; margin-bottom: 8px; }
  .services-list li::before, .detail-list li::before {
    content: ""; position: absolute; left: 0; top: 5px; width: 10px; height: 10px;
    border-radius: 50%; background: var(--teal);
  }
  .booking {
    position: absolute; color: var(--white); display: flex; align-items: center; gap: 12px;
  }
  .booking__label { font-style: italic; font-weight: 700; font-size: 15px; }
  .booking__phone { color: var(--yellow); font-weight: 700; font-size: 22px; display: flex; align-items: center; gap: 8px; white-space: nowrap; }
  .booking__phone svg { width: 14px; height: 14px; }
  .postcard--front .booking { left: 333px; top: 423px; }

  /* back */
  .specials-title {
    position: absolute; left: 10px; top: 16px; width: 374px; height: 52px;
    border-radius: 26px;
    background: linear-gradient(90deg, var(--teal-light) 0%, var(--teal) 60%, var(--teal-dark) 100%);
    font-family: "Mulish", sans-serif; font-weight: 800; font-size: 23px;
    color: var(--white); line-height: 52px; padding-left: 28px;
  }
  .specials-title .dark { color: var(--ink); }
  .about-tab {
    position: absolute; left: 0; top: 96px; width: 103px; height: 27px;
    background: var(--ink); border-radius: 0 14px 14px 0;
    color: var(--yellow); font-weight: 700; font-size: 16px; line-height: 27px; padding-left: 16px;
  }
  .about-text {
    position: absolute; left: 16px; top: 138px; width: 382px;
    font-size: 9.6px; line-height: 12.4px; color: var(--text);
  }
  .detail-list {
    position: absolute; left: 20px; top: 220px; width: 296px; list-style: none;
    font-size: 9.6px; line-height: 12.4px; color: var(--text);
  }
  .detail-list li { position: relative; padding-left: 22px; margin-bottom: 7px; }
  .detail-list li::before { top: 1px; left: 0; }
  .postcard--back .booking { left: 36px; top: 385px; flex-direction: column; align-items: flex-start; gap: 2px; }
  .postcard--back .booking__phone { font-size: 24px; }
  .stamp-box { position: absolute; left: 712px; top: 28px; width: 72px; height: 92px; border: 1px solid #888; }
  .address-line { position: absolute; left: 520px; width: 262px; height: 1px; background: #777; }
  .address-line--1 { top: 220px; }
  .address-line--2 { top: 269px; }
  .address-line--3 { top: 318px; }
</style>
</head>
<body>

<section class="postcard postcard--front">
  <svg class="shapes" viewBox="0 0 826 455" aria-hidden="true">
    <defs>
      <linearGradient id="photoFade" x1="0" x2="1">
        <stop offset="0" stop-color="#ffffff" stop-opacity="0"/>
        <stop offset=".3" stop-color="#c9cfd3"/>
        <stop offset="1" stop-color="#9ea7ad"/>
      </linearGradient>
      <linearGradient id="tealBand" x1="0" x2="1">
        <stop offset="0" stop-color="#1b9aa4"/>
        <stop offset=".6" stop-color="#4cc3cc"/>
        <stop offset="1" stop-color="#139099"/>
      </linearGradient>
      <linearGradient id="personTone" x1="0" y1="0" x2="0" y2="1">
        <stop offset="0" stop-color="#c79a7c"/>
        <stop offset=".55" stop-color="#e8d46a"/>
        <stop offset="1" stop-color="#3f67b0"/>
      </linearGradient>
    </defs>
    <path d="M340,0 H826 V200 C640,222 480,205 340,170 Z" fill="url(#photoFade)" role="img" aria-label="Photo of a worker pressure washing a pavement"/>
    <path d="M0,66 C200,110 400,185 650,214 L650,222 C400,198 200,128 0,86 Z" fill="var(--yellow)"/>
    <path d="M0,108 C250,170 500,232 826,200 L826,335 C640,282 380,262 0,318 Z" fill="url(#tealBand)"/>
    <path d="M0,318 C380,262 640,282 826,335" fill="none" stroke="var(--ink)" stroke-width="4"/>
    <path d="M12,455 V230 C60,190 230,180 300,230 V455 Z" fill="url(#personTone)" role="img" aria-label="Photo of a smiling cleaner holding a spray bottle and sponge"/>
    <path d="M275,415 C450,400 650,408 826,438" fill="none" stroke="var(--teal)" stroke-width="4"/>
    <path d="M270,422 C450,408 650,414 826,446 V455 H270 Z" fill="var(--bar)"/>
  </svg>
  <div class="brand"><span class="brand__mark"></span>Northgate Tidy Works</div>
  <div class="services-tab"><span class="accent">Our</span> Services</div>
  <ul class="services-list">
    <li>Air duct cleaning</li>
    <li>Dryer vent cleaning &amp; Pressure washing</li>
  </ul>
  <div class="booking">
    <span class="booking__label">For Booking Call now</span>
    <span class="booking__phone">
      <svg viewBox="0 0 24 24" fill="#fff"><path d="M6.6 10.8a15 15 0 0 0 6.6 6.6l2.2-2.2a1 1 0 0 1 1-.25 11.4 11.4 0 0 0 3.6.57 1 1 0 0 1 1 1V20a1 1 0 0 1-1 1A17 17 0 0 1 3 4a1 1 0 0 1 1-1h3.5a1 1 0 0 1 1 1c0 1.25.2 2.45.57 3.6a1 1 0 0 1-.25 1z"/></svg>
      0147 258 369
    </span>
  </div>
</section>

<section class="postcard postcard--back">
  <svg class="shapes" viewBox="0 0 826 455" aria-hidden="true">
    <path d="M375,0 C420,120 430,300 390,455" fill="none" stroke="var(--teal)" stroke-width="10"/>
    <path d="M392,0 C436,120 446,300 406,455" fill="none" stroke="var(--yellow)" stroke-width="6"/>
    <path d="M404,0 C448,120 458,300 418,455" fill="none" stroke="var(--ink)" stroke-width="6"/>
    <path d="M0,368 C100,355 200,352 300,356" fill="none" stroke="var(--teal)" stroke-width="6"/>
    <path d="M0,378 C100,365 200,362 300,366 L300,455 H0 Z" fill="var(--bar)"/>
    <circle cx="322" cy="388" r="70" fill="#dfe6ea" stroke="#2f7fc0" stroke-width="4" role="img" aria-label="Photo of a surface cleaner washing a patio"/>
  </svg>
  <div class="specials-title">Pressure <span class="dark">washing specials</span></div>
  <div class="about-tab">About Us</div>
  <p class="about-text">Lorem ipsum dolor sit amet, consectetuer adipiscing elit. Aenean commodo ligula eget dolor. Aenean massa. Cum sociis natoque penatibus et magnis dis parturient montes, nascetur ridiculus mus. Donec quam felis, ultricies nec, pellentesque eu, pretium quis, sem. Nulla consequat massa quis enim. Donec pede justo, fringilla vel, aliquet nec, vulputate eget, arcu. In enim justo, rhoncus ut, imperdiet a, venenatis vitae, justo.</p>
  <ul class="detail-list">
    <li>Nullam dictum felis eu pede mollis pretium. Integer tincidunt. Cras dapibus. Vivamus elementum semper nisi.</li>
    <li>Aenean vulputate eleifend tellus.<br>Aenean leo ligula, porttitor eu, consequat vitae, eleifend ac, enim.</li>
    <li>Aliquam lorem ante, dapibus in, viverra quis, feugiat a, tellus. Phasellus viverra nulla ut metus varius laoreet. Quisque rutrum.</li>
  </ul>
  <div class="booking">
    <span class="booking__label">For Booking Call now</span>
    <span class="booking__phone">
      <svg viewBox="0 0 24 24" fill="#fff"><path d="M6.6 10.8a15 15 0 0 0 6.6 6.6l2.2-2.2a1 1 0 0 1 1-.25 11.4 11.4 0 0 0 3.6.57 1 1 0 0 1 1 1V20a1 1 0 0 1-1 1A17 17 0 0 1 3 4a1 1 0 0 1 1-1h3.5a1 1 0 0 1 1 1c0 1.25.2 2.45.57 3.6a1 1 0 0 1-.25 1z"/></svg>
      0147 258 369
    </span>
  </div>
  <div class="stamp-box"></div>
  <div class="address-line address-line--1"></div>
  <div class="address-line address-line--2"></div>
  <div class="address-line address-line--3"></div>
</section>

</body>
</html>
```